Digitalization Training Site - Lumo Theme (mandatory)

Hi,
I have a Lumo theme website running on Wordpress and I need a design.

Designs must be possible with standard Lumo theme and minimal/no CSS customization or similar. if this is required please note this in submission. Also, please note mobile and device usage which must be universal.

Lumo Theme:
https://www.crispcanvas.com

Target Market: education, online training, IT training, digitalization, digital transformation, disruption

Target Group: IT students, IT Management students, IT companies showing examples, IT companies recruiting, lectures, trainers, training companies

Look and Feel:
- Elegant, Playful, Fresh, Plain, Personable, Economical

Main Colors:
- Background: mainly white/light grey (like logo), a few parts maybe in orange (like the logo colors)
- design elements: logo colors (grey, dark yellow – orange, and one extra color: a darker blue that fits to the logo colors)
- text: grey, black, white - depending on background, good readable

Form
- round buttons
- full with
- responsive for desktop, tablet and mobile (lumo is supporting this ;)
- animation like on the Lumo layout for e-courses (see below)

I have attached:
- logo files (ai, png, jpg, eps)
- some design parts that I like (samples for blocks)

To be delivered:
- lumo layout (zipped json files)
- all pictures, icons, and illustrations (high res. : ai, psd, eps, jpg, png)

There is a Lumo Layout for e-courses that is partly interesting you can find it here:
- https://www.crispcanvas.com/blog/lumo-resources/download-a-free-breathtaking-learning-management-lms-layout-pack-for-lumo
- Can be used as idea for building blocks

I need at least 20 building blocks (see examples I uploaded) for homepage, landing page, shop, product page, marketing, landing, about us, etc. The building blocks could be
- Slider (for home page) (I like the light bulbs in one of the examples)
- Content blocks with illustrations
- Get started area (free & premium)
- Choose a plan
- Our Process (5-6 steps)
- Cartlane shop page
- Cartlane product page
- We offer
- Footer
I like the footer animation in this example: http://demo.lumoplus.com/lumo-edu//gallery/
- Contact
- see Lumo Layout example for more Blocks
NOT:
- Newsletter

Best regards
Anselm

Target Market(s)

Industry/Entity Type

Training

Coding

Coded - Design and coding required

Number of Pages Required

5+ page

Font styles to use
Serif

Colors
ffcf3e
ffc214
faa54b
f78f20
f68e4e
f37122
3276b5
99b9da
959595

Requirements
Must have
• Designs must be possible with standard Lumo theme and minimal/no CSS customization or similar. if this is required please note this in submission. Also, please note mobile and device usage which must be universal.
• adopt design preference (logo colors etc. - see big text)
• To be delivered:
• - lumo layout (zipped json files)
• - all pictures, icons, and illustrations (high res. : ai, psd, eps, jpg, png)
Nice to have
• Ideas for good design for a online-course site

```html
<!DOCTYPE html>
<html lang="en">
<head>
<meta charset="utf-8">
<title>Northbeam Digital School</title>
<link href="https://fonts.googleapis.com/css2?family=Lato:wght@300;400;700;900&display=swap" rel="stylesheet">
<style>
:root{
  --black:#111111;
  --white:#ffffff;
  --grey:#959595;
  --grey-dark:#444444;
  --grey-light:#ececec;
  --orange:#f37122;
  --orange-mid:#f78f20;
  --orange-soft:#faa54b;
  --yellow:#ffc214;
  --blue:#3276b5;
  --blue-soft:#99b9da;
  --footer:#3a3a3a;
}
*{box-sizing:border-box;margin:0;padding:0}
html,body{width:1200px;height:3612px;overflow:hidden}
body{font-family:'Lato',sans-serif;color:var(--grey-dark);background:var(--white);position:relative}
.nav{position:absolute;top:0;left:0;width:1200px;height:40px;background:var(--black);display:flex;justify-content:center;gap:34px;align-items:center;z-index:2}
.nav a{color:var(--white);font-size:13px;text-decoration:none;letter-spacing:.5px}
.nav a.active{color:var(--orange-mid)}
.hero{position:absolute;top:0;left:0;width:1200px;height:660px}
.hero-photo{position:absolute;inset:0;background:linear-gradient(120deg,#3b4650 0%,#6d7780 40%,#9aa0a4 65%,#5d6770 100%)}
.hero-shade{position:absolute;inset:0;background:rgba(20,24,30,.35)}
.brand{position:absolute;top:240px;left:0;width:1200px;display:flex;justify-content:center;align-items:center;gap:16px}
.brand-dot{width:56px;height:56px;border-radius:50%;background:var(--orange)}
.brand-name{font-size:40px;font-weight:700;color:var(--white)}
.hero-title{position:absolute;top:318px;width:1200px;text-align:center;color:var(--white);font-size:36px;font-weight:900;letter-spacing:1px}
.hero-actions{position:absolute;top:392px;width:1200px;display:flex;justify-content:center;gap:24px}
.btn{display:inline-block;height:40px;line-height:40px;padding:0 36px;border-radius:20px;font-size:14px;font-weight:700;color:var(--white);text-decoration:none}
.btn-ghost{border:2px solid var(--white);line-height:36px}
.btn-orange{background:var(--orange)}
.hero-down{position:absolute;top:578px;left:578px}
.services{position:absolute;top:660px;width:1200px;height:360px;display:flex;justify-content:center;gap:50px;padding-top:60px}
.service{width:200px;text-align:center}
.service svg{display:block;margin:0 auto 22px}
.service h3{font-size:18px;font-weight:700;color:var(--grey-dark);margin-bottom:12px;line-height:1.15}
.service p{font-size:12px;line-height:1.55;color:var(--grey)}
.section-title{position:absolute;width:1200px;text-align:center;font-size:36px;font-weight:900;color:var(--black)}
.projects{position:absolute;top:1108px;left:120px;display:flex;gap:26px}
.project{width:220px;height:180px}
.view-more{position:absolute;top:1350px;left:508px;width:184px;height:40px;line-height:40px;text-align:center;background:var(--blue);color:var(--white);font-size:13px;font-weight:700;border-radius:4px}
.team{position:absolute;top:1460px;width:1200px;height:540px;background:linear-gradient(180deg,var(--orange-mid) 0%,var(--orange-soft) 100%)}
.team .section-title{top:50px;color:var(--white)}
.team-intro{position:absolute;top:112px;left:260px;width:680px;text-align:center;color:var(--white);font-size:13px;line-height:1.6}
.members{position:absolute;top:216px;left:124px;display:flex;gap:56px}
.member{width:192px;text-align:center}
.member-photo{width:192px;height:192px;border-radius:50%;border:5px solid var(--white)}
.member h4{margin-top:24px;font-size:15px;font-weight:900;color:var(--white)}
.member p{font-size:12px;color:var(--white);margin-top:4px}
.gallery{position:absolute;top:2000px;width:1200px;height:580px}
.gallery div{position:absolute}
.testimonials{position:absolute;top:2580px;width:1200px;height:412px;background:var(--blue);color:var(--white);text-align:center}
.testimonials .section-title{top:70px;color:var(--white);font-size:32px}
.quote{position:absolute;top:146px;left:240px;width:720px;font-size:17px;font-style:italic;line-height:1.75}
.author{position:absolute;top:276px;width:1200px;font-size:15px;color:var(--blue-soft)}
.dots{position:absolute;top:344px;width:1200px;display:flex;justify-content:center;gap:8px}
.dots span{width:8px;height:8px;border-radius:50%;background:var(--blue-soft)}
.dots span:first-child{background:var(--white)}
.arrow{position:absolute;top:176px}
.contact .section-title{top:3030px;font-size:30px}
.contact-text{position:absolute;top:3088px;left:380px;width:440px;text-align:center;font-size:13px;line-height:1.6;color:var(--grey)}
.field{position:absolute;background:var(--grey-light);font-size:13px;color:var(--grey);padding:0 14px;line-height:44px}
.send{position:absolute;top:3420px;left:922px;width:120px;height:40px;line-height:36px;text-align:center;border:2px solid var(--orange);color:var(--orange);font-size:13px;font-weight:700;border-radius:20px}
.footer{position:absolute;top:3540px;width:1200px;height:72px;background:var(--footer);color:#bbbbbb;font-size:12px}
.footer p{position:absolute;left:132px;top:28px}
.social{position:absolute;right:150px;top:26px;display:flex;gap:18px}
.social span{width:18px;height:18px;border-radius:50%;background:#bbbbbb}
</style>
</head>
<body>
<header class="hero">
  <div class="hero-photo" role="img" aria-label="Photo of a man working on a laptop at a desk in a bright office"></div>
  <div class="hero-shade"></div>
  <nav class="nav">
    <a class="active" href="#">HOME</a><a href="#">ABOUT US</a><a href="#">OUR SERVICES</a><a href="#">WHY US</a><a href="#">BLOGS</a><a href="#">CONTACT</a>
  </nav>
  <div class="brand"><span class="brand-dot"></span><span class="brand-name">Northbeam Digital School</span></div>
  <h1 class="hero-title">WE ARE A DIGITALISATION TRAINING</h1>
  <div class="hero-actions"><a class="btn btn-ghost" href="#">CLICK HERE</a><a class="btn btn-orange" href="#">START NOW</a></div>
  <svg class="hero-down" width="44" height="44" viewBox="0 0 44 44"><circle cx="22" cy="22" r="20" fill="none" stroke="#fff" stroke-width="2"/><path d="M14 18l8 8 8-8" fill="none" stroke="#fff" stroke-width="2.5"/></svg>
</header>

<section class="services">
  <div class="service">
    <svg width="70" height="56" viewBox="0 0 70 56" fill="none" stroke="#f78f20" stroke-width="3"><rect x="10" y="4" width="50" height="34" rx="2"/><path d="M2 44h66v4H2z"/><path d="M20 16h30M20 24h20"/></svg>
    <h3>ONLINE TRAINING</h3>
    <p>Learn at your own pace with live sessions, guided projects and mentor feedback from anywhere.</p>
  </div>
  <div class="service">
    <svg width="70" height="56" viewBox="0 0 70 56" fill="none" stroke="#f78f20" stroke-width="3"><rect x="26" y="4" width="40" height="28"/><circle cx="14" cy="14" r="7"/><path d="M4 52V32q0-8 10-8h18M14 52V38"/></svg>
    <h3>IT TRAINING</h3>
    <p>Hands-on courses in networks, cloud and software that prepare students for real roles in IT teams.</p>
  </div>
  <div class="service">
    <svg width="70" height="56" viewBox="0 0 70 56" fill="none" stroke="#f78f20" stroke-width="3"><rect x="22" y="14" width="26" height="26"/><path d="M28 14V4M42 14V4M28 50V40M42 50V40M12 22h10M12 34h10M48 22h10M48 34h10"/></svg>
    <h3>DIGITALISATION</h3>
    <p>Move paper processes to smart digital workflows with tools your whole team can adopt quickly.</p>
  </div>
  <div class="service">
    <svg width="70" height="56" viewBox="0 0 70 56" fill="none" stroke="#f78f20" stroke-width="3"><circle cx="20" cy="28" r="12"/><circle cx="50" cy="28" r="12"/><circle cx="20" cy="28" r="4"/><circle cx="50" cy="28" r="4"/><path d="M32 28h6"/></svg>
    <h3>DIGITAL TRANSFORMATION</h3>
    <p>Plan and lead change with strategy, data and culture so every department grows with new technology.</p>
  </div>
</section>

<h2 class="section-title" style="top:1030px">OUR PROJECTS</h2>
<div class="projects">
  <div class="project" role="img" aria-label="Photo of colleagues talking at a laptop" style="background:linear-gradient(135deg,#c9c4bd,#7a6f66)"></div>
  <div class="project" role="img" aria-label="Photo of a group meeting around a table" style="background:linear-gradient(135deg,#b8b2aa,#4e4a46)"></div>
  <div class="project" role="img" aria-label="Photo of a hand touching a glowing digital screen" style="background:linear-gradient(135deg,#2c5d8a,#7fb3d8)"></div>
  <div class="project" role="img" aria-label="Photo of a laptop with a digital overlay" style="background:linear-gradient(135deg,#d6d0c8,#8c7f72)"></div>
</div>
<a class="view-more" href="#">VIEW MORE</a>

<section class="team">
  <h2 class="section-title">OUR TEAM</h2>
  <p class="team-intro">Our trainers bring years of industry practice to every class. They guide students, companies and lecturers through modern tools, clear methods and real projects so that learning turns into results you can use at work the very next day.</p>
  <div class="members">
    <div class="member"><div class="member-photo" role="img" aria-label="Portrait of a team member" style="background:linear-gradient(160deg,#9aa3ab,#4d5660)"></div><h4>MEMBER NAME</h4><p>Lead Trainer</p></div>
    <div class="member"><div class="member-photo" role="img" aria-label="Portrait of a team member" style="background:linear-gradient(160deg,#b9b4ae,#5b534c)"></div><h4>MEMBER NAME</h4><p>Cloud Instructor</p></div>
    <div class="member"><div class="member-photo" role="img" aria-label="Portrait of a team member" style="background:linear-gradient(160deg,#e4e0dc,#6f6a72)"></div><h4>MEMBER NAME</h4><p>Course Designer</p></div>
    <div class="member"><div class="member-photo" role="img" aria-label="Portrait of a team member" style="background:linear-gradient(160deg,#c8c6c2,#3f4448)"></div><h4>MEMBER NAME</h4><p>Strategy Coach</p></div>
  </div>
</section>

<section class="gallery">
  <div role="img" aria-label="Photo of a hand holding a phone with a network of connected lines" style="left:0;top:0;width:600px;height:580px;background:linear-gradient(135deg,#1d3d66,#6c9cc9 55%,#d9a86a)"></div>
  <div role="img" aria-label="Photo of hands typing on a laptop keyboard" style="left:600px;top:0;width:600px;height:290px;background:linear-gradient(135deg,#4a3d35,#a08c78)"></div>
  <div role="img" aria-label="Photo of people working together on laptops and tablets" style="left:600px;top:290px;width:600px;height:290px;background:linear-gradient(135deg,#8a8580,#3c3835)"></div>
</section>

<section class="testimonials">
  <h2 class="section-title">TESTIMONIALS</h2>
  <svg class="arrow" style="left:34px" width="20" height="32" viewBox="0 0 20 32"><path d="M16 4L4 16l12 12" fill="none" stroke="#fff" stroke-width="4"/></svg>
  <svg class="arrow" style="right:34px" width="20" height="32" viewBox="0 0 20 32"><path d="M4 4l12 12L4 28" fill="none" stroke="#fff" stroke-width="4"/></svg>
  <p class="quote">“ Maecenas aliquet velit vel turpis Mauris neque metus malesuada nec ultricies ac amet porttitor mattis enim in massa libero interdum nec interdum vel blandit sed nulla in ullamcorper est eget tempor cursus neque mi ”</p>
  <p class="author">- By Author Name</p>
  <div class="dots"><span></span><span></span><span></span><span></span></div>
</section>

<section class="contact">
  <h2 class="section-title">CONTACT US</h2>
  <p class="contact-text">Questions about a course or a team programme? Send us a message and we will reply within one working day.</p>
  <div class="field" style="top:3184px;left:150px;width:440px;height:44px">Your Name</div>
  <div class="field" style="top:3184px;left:610px;width:440px;height:44px">Email address</div>
  <div class="field" style="top:3248px;left:150px;width:900px;height:150px">Message</div>
  <div class="send">SEND</div>
</section>

<footer class="footer">
  <p>© 2018 Northbeam Digital School. All rights reserved. Terms of use.</p>
  <div class="social"><span></span><span></span><span></span><span></span><span></span></div>
</footer>
</body>
</html>
```